Buch-/eBook-Cover für Esoterikbuch
Alle meine Änderungswünsche wurden zeitnah umgesetzt. Als es nach der Dateiübergabe technische Probleme gab, weil ich den Buchinhalt falsch formatiert hatte, hat die Designerin viel Geduld bewiesen und das Cover dann klaglos an die neuen Formate angepasst. Ich werde jederzeit gerne wieder mit ihr zusammenarbeiten.
Zielgruppe
Ebook- und Taschenbuchcover für ein Esoterikbuch über Quantenheilung auf Lesora. Details befinden sich im Anhang.
Aufgabenstellung
Keine besonderen Vorgaben.

```html
<!DOCTYPE html>
<html lang="de">
<head>
<meta charset="utf-8">
<title>Quantenheilung und Bewusstsein – Cover</title>
<link href="https://fonts.googleapis.com/css2?family=Tulpen+One&family=Dosis:wght@500&display=swap" rel="stylesheet">
<style>
  :root {
    --stage-bg: #ecebe8;
    --navy-deep: #06133f;
    --navy: #0d2a7a;
    --blue: #1c5ad0;
    --cyan-glow: #a9ecff;
    --ice: #5fc4f2;
    --text-light: #ffffff;
  }
  * { margin: 0; padding: 0; box-sizing: border-box; }
  html, body {
    width: 1200px;
    height: 800px;
    overflow: hidden;
    background: var(--stage-bg);
  }
  .stage {
    position: relative;
    width: 1200px;
    height: 800px;
    display: flex;
    align-items: center;
    justify-content: center;
  }
  .book-cover {
    position: relative;
    width: 440px;
    height: 760px;
    overflow: hidden;
    color: var(--text-light);
  }
  .cover-artwork {
    position: absolute;
    inset: 0;
    background:
      radial-gradient(ellipse 38% 14% at 18% 57%, rgba(255,255,255,0.95) 0%, var(--cyan-glow) 35%, rgba(95,196,242,0) 100%),
      radial-gradient(ellipse 90% 35% at 30% 60%, rgba(95,196,242,0.75) 0%, rgba(28,90,208,0) 70%),
      linear-gradient(180deg, var(--navy-deep) 0%, var(--navy) 30%, var(--blue) 52%, #3aa3e6 62%, var(--blue) 78%, var(--navy) 100%);
  }
  .title {
    position: absolute;
    right: 46px;
    top: 30px;
    font-family: "Tulpen One", sans-serif;
    font-size: 128px;
    line-height: 0.86;
    letter-spacing: 6px;
    text-align: right;
    text-transform: uppercase;
  }
  .title-line { display: block; }
  .title-addition {
    position: absolute;
    right: 48px;
    top: 268px;
    font-family: "Tulpen One", sans-serif;
    font-size: 42px;
    letter-spacing: 1.5px;
    text-transform: uppercase;
  }
  .tagline {
    position: absolute;
    right: 52px;
    top: 348px;
    font-family: "Tulpen One", sans-serif;
    font-size: 34px;
    line-height: 1.08;
    letter-spacing: 0.5px;
    text-align: right;
  }
  .author {
    position: absolute;
    right: 46px;
    bottom: 24px;
    font-family: "Dosis", sans-serif;
    font-weight: 500;
    font-size: 17px;
    letter-spacing: 0.3px;
  }
</style>
</head>
<body>
  <main class="stage">
    <section class="book-cover">
      <div class="cover-artwork" role="img" aria-label="Silhouette eines gehenden Menschen auf einem leuchtenden blauen Lichtgitter, das in einen hellen Tunnel führt"></div>
      <h1 class="title">
        <span class="title-line">Quanten</span>
        <span class="title-line">Heilung</span>
      </h1>
      <p class="title-addition">und Bewusstsein</p>
      <p class="tagline">Wie Sie Zugriff auf die<br>Informationsebene<br>der Realität nehmen</p>
      <p class="author">Konrad Falkenried</p>
    </section>
  </main>
</body>
</html>
```